Business Card Design Project

Refresh of logo attached. Require text underneath to be more ledgible, crisper & cleaner.

Overall, staying with same colour scheme need a brighter, crisper, easily readible business card style.

Industry/Entity Type

Business

```html
<!DOCTYPE html>
<html lang="en">
<head>
<meta charset="utf-8">
<title>ALTEA Business Card Set</title>
<link rel="stylesheet" href="https://fonts.googleapis.com/css2?family=Crimson+Text:wght@400;600&family=Open+Sans:wght@400;600&display=swap">
<style>
  :root {
    --backdrop: #3b2f28;
    --card-white: #ffffff;
    --card-charcoal: #3b3b3b;
    --card-teal: #2b4f5d;
    --teal-dark: #27505f;
    --teal-bright: #2283a2;
    --ink: #3a3a3a;
    --ink-soft: #4a4a4a;
    --rule: #5a1f1f;
    --label: #ffffff;
    --muted-url: #555555;
  }
  * { margin: 0; padding: 0; box-sizing: border-box; }
  html, body { width: 1200px; height: 773px; overflow: hidden; }
  body { background: var(--backdrop); position: relative; font-family: "Open Sans", sans-serif; }

  .card { position: absolute; width: 474px; height: 271px; overflow: hidden; box-shadow: 0 3px 8px rgba(0,0,0,.45); }
  .card--front { left: 126px; top: 109px; background: var(--card-white); }
  .card--back-white { left: 643px; top: 107px; background: var(--card-white); }
  .card--back-charcoal { left: 126px; top: 393px; background: var(--card-charcoal); }
  .card--back-teal { left: 638px; top: 389px; background: var(--card-teal); }

  .set-label { position: absolute; color: var(--label); font-family: "Open Sans", sans-serif; font-size: 34px; line-height: 1; }
  .set-label--one { left: 993px; top: 60px; }
  .set-label--two { left: 147px; top: 700px; }
  .set-label--three { left: 1005px; top: 686px; }

  .brand { display: flex; align-items: center; gap: 12px; }
  .brand__mark { width: 44px; height: 44px; background: var(--teal-bright); flex: none; }
  .brand__name { font-family: "Crimson Text", serif; font-weight: 600; color: var(--ink); letter-spacing: 1px; line-height: 1; }

  .front__lockup { position: absolute; left: 111px; top: 42px; width: 256px; }
  .front__lockup .brand__name { font-size: 58px; }
  .front__rule { height: 2px; background: var(--rule); margin-top: 6px; }
  .front__tagline { margin-top: 5px; font-size: 9.5px; letter-spacing: .6px; color: var(--ink-soft); white-space: nowrap; }
  .front__tagline em { font-style: normal; color: var(--teal-bright); }

  .front__person { position: absolute; left: 29px; top: 212px; }
  .front__name { font-family: "Crimson Text", serif; font-weight: 600; font-size: 21px; color: var(--teal-dark); line-height: 1.1; white-space: nowrap; }
  .front__title { font-size: 11.5px; color: var(--ink); margin-top: 3px; }
  .front__divider { position: absolute; left: 226px; top: 212px; width: 1.5px; height: 42px; background: var(--teal-bright); }
  .front__contacts { position: absolute; right: 24px; top: 215px; font-size: 11px; color: var(--ink); line-height: 20px; }
  .contact-row { display: flex; gap: 8px; align-items: center; white-space: nowrap; }
  .contact { display: inline-flex; align-items: center; gap: 4px; }
  .contact svg { width: 11px; height: 11px; fill: var(--ink); }

  .back__lockup { position: absolute; left: 0; right: 0; display: flex; justify-content: center; }
  .back__lockup .brand__name { font-size: 44px; }
  .back-white__lockup { top: 100px; }
  .back-white__lockup .brand__name { color: var(--teal-dark); }
  .back-charcoal__lockup { top: 100px; }
  .back-charcoal__lockup .brand__name { color: var(--teal-dark); }
  .back-charcoal__lockup .brand__mark { background: var(--teal-dark); }

  .url { position: absolute; font-size: 11.5px; letter-spacing: 5px; white-space: nowrap; }
  .back-white__url { left: 0; right: 0; top: 196px; text-align: center; color: var(--teal-bright); }
  .back-charcoal__url { left: 0; right: 0; top: 244px; text-align: center; color: var(--muted-url); }
  .back-teal__url { left: 45px; top: 249px; color: var(--card-white); letter-spacing: 3.5px; }

  .back-teal__lockup { position: absolute; right: 30px; top: 96px; }
  .back-teal__lockup .brand__mark { width: 70px; height: 70px; }
  .back-teal__lockup .brand__name { font-size: 64px; color: var(--teal-bright); }
</style>
</head>
<body>
  <span class="set-label set-label--one">Back 1</span>
  <span class="set-label set-label--two">Back 2</span>
  <span class="set-label set-label--three">Back 3</span>

  <section class="card card--front" aria-label="Card front">
    <div class="front__lockup">
      <div class="brand">
        <span class="brand__mark"></span>
        <span class="brand__name">ALTEA</span>
      </div>
      <div class="front__rule"></div>
      <p class="front__tagline">ASSOCIATION OF LICENSED <em>TRUSTEE &amp; ESTATE ADVISORS</em></p>
    </div>

    <div class="front__person">
      <p class="front__name">Daniel R. Whitford</p>
      <p class="front__title">Licensed Estate Advisor</p>
    </div>
    <div class="front__divider"></div>
    <div class="front__contacts">
      <div class="contact-row">
        <span class="contact">
          <svg viewBox="0 0 24 24" aria-hidden="true"><path d="M6.6 10.8a15.1 15.1 0 0 0 6.6 6.6l2.2-2.2a1 1 0 0 1 1-.25 11.4 11.4 0 0 0 3.6.57 1 1 0 0 1 1 1V20a1 1 0 0 1-1 1A17 17 0 0 1 3 4a1 1 0 0 1 1-1h3.5a1 1 0 0 1 1 1c0 1.25.2 2.45.57 3.57a1 1 0 0 1-.25 1z"/></svg>
          (555) 201 4470
        </span>
        <span class="contact">
          <svg viewBox="0 0 24 24" aria-hidden="true"><path d="M8 1h8a2 2 0 0 1 2 2v18a2 2 0 0 1-2 2H8a2 2 0 0 1-2-2V3a2 2 0 0 1 2-2zm0 3v14h8V4z"/></svg>
          (555) 309 8812
        </span>
      </div>
      <div class="contact-row">
        <span class="contact">
          <svg viewBox="0 0 24 24" aria-hidden="true"><path d="M2 5h20v14H2zm2 2v.5l8 5 8-5V7l-8 5z"/></svg>
          daniel@altea.test
        </span>
        <span class="contact">
          <svg viewBox="0 0 24 24" aria-hidden="true"><path d="M12 2a10 10 0 1 0 0 20 10 10 0 0 0 0-20zm6.9 9h-3a15 15 0 0 0-1.3-5.6A8 8 0 0 1 18.9 11zM12 4c.9 1.2 1.8 3.6 1.9 7h-3.8c.1-3.4 1-5.8 1.9-7zM9.4 5.4A15 15 0 0 0 8.1 11h-3a8 8 0 0 1 4.3-5.6zM5.1 13h3a15 15 0 0 0 1.3 5.6A8 8 0 0 1 5.1 13zm6.9 7c-.9-1.2-1.8-3.6-1.9-7h3.8c-.1 3.4-1 5.8-1.9 7zm2.6-1.4a15 15 0 0 0 1.3-5.6h3a8 8 0 0 1-4.3 5.6z"/></svg>
          www.altea.test
        </span>
      </div>
    </div>
  </section>

  <section class="card card--back-white" aria-label="Card back, white">
    <div class="back__lockup back-white__lockup">
      <div class="brand">
        <span class="brand__mark"></span>
        <span class="brand__name">ALTEA</span>
      </div>
    </div>
    <p class="url back-white__url">www.altea.test</p>
  </section>

  <section class="card card--back-charcoal" aria-label="Card back, charcoal">
    <div class="back__lockup back-charcoal__lockup">
      <div class="brand">
        <span class="brand__mark"></span>
        <span class="brand__name">ALTEA</span>
      </div>
    </div>
    <p class="url back-charcoal__url">www.altea.test</p>
  </section>

  <section class="card card--back-teal" aria-label="Card back, teal">
    <div class="back-teal__lockup">
      <div class="brand">
        <span class="brand__mark"></span>
        <span class="brand__name">ALTEA</span>
      </div>
    </div>
    <p class="url back-teal__url">www.altea.test</p>
  </section>
</body>
</html>
```